Need Amazing Website for Consulting Company

We need an amazing website design for a Human Resources Consulting Company. This will be geared towards a more professional crowd, but we don't want it to be overly corporate and stuffy: Just, clean and professional and amazing. Please use the video link below for further instruction.

http://clipvarn.example/t/kzQmPoLe7

Thank You.

PS Logo file has been attached.

Target Market(s)

The target marketing is small business owners who have employees. These owners cant afford an in-house HR person so they would hire this client to consult and do the work for them.

Industry/Entity Type

It Company

Font styles to use
Sans Serif

Requirements
Must have
• Please watch video:

Must have spot for video on homepage.
Nice to have
• Clean, professional, but not overly corporate, we want a personal and fun feel to this site a bit to separate them from all the other executive type sites. This site should have some LIFE to it and reflect a local brand that is doing great things.
Should not have
• Should not be just a corporate site, should not be overly stuffy, should not be overly boring.

```html
<!DOCTYPE html>
<html lang="en">
<head>
<meta charset="utf-8">
<title>Mesa Ridge HR Consulting</title>
<link rel="stylesheet" href="https://fonts.googleapis.com/css2?family=Open+Sans:wght@400;600;700&display=swap">
<style>
:root{
  --accent:#e0475a;
  --ink:#2b2b2b;
  --muted:#6b6b6b;
  --dark:#2f2f2f;
  --navbar:#2a2a2a;
  --pale:#efefef;
  --line:#dedede;
  --white:#fff;
}
*{box-sizing:border-box;margin:0;padding:0}
html,body{width:1200px;height:900px;overflow:hidden;background:var(--white);font-family:"Open Sans",Arial,sans-serif;color:var(--ink)}
.page{position:relative;width:1200px;height:900px}
.abs{position:absolute}
.brand{left:0;width:1200px;top:14px;text-align:center}
.brand-name{display:inline-flex;align-items:center;gap:8px;font-weight:700;font-size:22px;color:var(--ink);letter-spacing:.5px}
.brand-mark{width:14px;height:14px;background:var(--accent)}
.contact-line{left:0;width:1200px;top:80px;text-align:center;font-size:8px;color:var(--ink)}
.contact-line .label{color:var(--accent)}
.contact-line .sep{color:var(--accent);margin:0 6px}
.hero{left:272px;top:118px;width:657px;height:220px;background:linear-gradient(100deg,#c9cdd1 0%,#b7bcc0 35%,#8d8782 60%,#b8a59a 78%,#d8d9db 100%)}
.nav{left:326px;top:107px;width:548px;height:24px;background:var(--navbar);display:flex;border-bottom:1px dashed #777}
.nav a{color:var(--white);text-decoration:none;font-size:7px;font-weight:700;text-transform:uppercase;display:flex;align-items:center;padding:0 13px}
.nav a.active{background:var(--accent);padding:0 16px}
.video-frame{left:337px;top:149px;width:239px;height:155px;background:var(--white)}
.video{left:326px;top:154px;width:260px;height:145px;background:#333}
.video-bar{left:329px;top:279px;width:254px;height:17px;background:#222;display:flex;align-items:center;gap:6px;padding:0 6px}
.video-track{flex:1;height:3px;background:#3c4a4c}
.video-time{font-size:5px;color:var(--white);background:#555;padding:0 2px}
.video-hd{font-size:6px;font-weight:700;color:#2ab4e0;font-style:normal}
.hero-title{left:600px;top:200px;font-size:15px;font-weight:700;color:var(--white)}
.hero-text{left:600px;top:226px;width:260px;font-size:8px;line-height:13px;color:var(--white);font-weight:600}
.btn{display:inline-flex;align-items:center;justify-content:center;background:var(--accent);color:var(--white);font-size:7px;font-weight:700;text-transform:uppercase;width:74px;height:20px;border-radius:2px}
.hero-btn{left:601px;top:273px}
.dots{left:591px;top:321px;display:flex;gap:2px}
.dots span{width:5px;height:5px;border-radius:50%;border:1px solid var(--white)}
.dots span.on{background:var(--white)}
.feature{top:360px;width:190px;height:175px;text-align:center}
.feature+.divider{}
.divider{top:360px;width:1px;height:175px;background:var(--line)}
.f-icon{width:62px;height:62px;border-radius:50%;border:2px solid var(--line);margin:11px auto 0;display:flex;align-items:center;justify-content:center}
.f-icon span{width:30px;height:30px;border-radius:50%}
.f-title{font-size:14px;margin-top:7px;color:var(--ink)}
.f-text{font-size:7.5px;line-height:12px;color:var(--muted);margin:4px auto 0;width:170px}
.f-btn{margin-top:14px}
.why{left:272px;top:562px;width:657px;height:163px;background:var(--pale)}
.why-media{left:326px;top:584px;width:180px;height:120px;background:linear-gradient(180deg,#4f8fd6 0%,#8fb7e0 45%,#9a9a95 60%,#d4d1cc 100%)}
.why-title{left:519px;top:581px;font-size:17px;color:var(--ink)}
.why-text{left:519px;top:606px;width:360px;font-size:7.5px;line-height:13.6px;color:var(--muted)}
.why-btn{left:518px;top:684px}
.footer{left:272px;top:727px;width:657px;height:171px;background:var(--dark)}
.f-col{top:740px;color:var(--white)}
.f-col h3{font-size:11px;font-weight:700;margin-bottom:6px}
.f-col li{list-style:none;font-size:7.5px;line-height:11px;color:#ddd}
.social{display:flex;gap:4px;margin-top:5px}
.social span{width:12px;height:12px;border-radius:50%;background:#6a6a6a}
.find-row{display:flex;gap:8px;font-size:7.5px;line-height:11px;color:#ddd;margin-bottom:8px}
.find-row svg{flex:none}
.f-rule{left:326px;top:867px;width:548px;height:1px;background:#444}
.copyright{left:0;width:1200px;top:875px;text-align:center;font-size:6.5px;color:#999}
</style>
</head>
<body>
<div class="page">
  <div class="abs brand"><span class="brand-name"><span class="brand-mark"></span>Mesa Ridge HR</span></div>
  <div class="abs contact-line"><span class="label">Email:</span> info@mesaridgehr.example<span class="sep">|</span><span class="label">Phone:</span> +41 000 55 120</div>

  <div class="abs hero" role="img" aria-label="Blurred photo of colleagues in an office"></div>
  <nav class="abs nav">
    <a class="active">Home</a><a>About us</a><a>Services</a><a>HR Consulting</a><a>News</a><a>Events</a><a>Projects</a><a>Gallery</a><a>Contact us</a>
  </nav>
  <div class="abs video-frame"></div>
  <div class="abs video">
    <svg width="260" height="125" viewBox="0 0 260 125">
      <g fill="none" stroke="#bbb" stroke-width="1.2">
        <rect x="107" y="42" width="34" height="55"/>
        <rect x="111" y="46" width="8" height="47"/>
        <rect x="122" y="46" width="15" height="16"/>
        <rect x="122" y="66" width="15" height="27"/>
      </g>
    </svg>
  </div>
  <div class="abs video-bar">
    <svg width="8" height="9"><path d="M0 0 L8 4.5 L0 9Z" fill="#fff"/></svg>
    <span class="video-time">02:29</span>
    <span class="video-track"></span>
    <span class="video-hd">HD</span>
  </div>
  <div class="abs hero-title">Mesa Ridge HR Consulting</div>
  <p class="abs hero-text">Lorem Ipsum is simply dummy text of the printing and typesetting industry. Lorem Ipsum has been the industry's standard dummy text ever since the 1500s....</p>
  <span class="abs btn hero-btn">Read more</span>
  <div class="abs dots"><span></span><span class="on"></span><span></span></div>

  <div class="abs feature" style="left:316px">
    <div class="f-icon"><span role="img" aria-label="Recruitment icon" style="background:#c98a5a"></span></div>
    <h2 class="f-title">Recruitment</h2>
    <p class="f-text">Lorem ipsum dolor sit amet, sed dia consetetur sadipscing elitr, sed diam nonumy eirmod.</p>
    <span class="btn f-btn">Read more</span>
  </div>
  <div class="abs divider" style="left:506px"></div>
  <div class="abs feature" style="left:503px">
    <div class="f-icon"><span role="img" aria-label="Office building icon" style="background:#8fa0ad"></span></div>
    <h2 class="f-title">Business Ideas</h2>
    <p class="f-text">Lorem ipsum dolor sit amet, sed dia consetetur sadipscing elitr, sed diam nonumy eirmod.</p>
    <span class="btn f-btn">Read more</span>
  </div>
  <div class="abs divider" style="left:695px"></div>
  <div class="abs feature" style="left:692px">
    <div class="f-icon"><span role="img" aria-label="Handshake icon" style="background:#d9a27a"></span></div>
    <h2 class="f-title">Our Methodology</h2>
    <p class="f-text">Lorem ipsum dolor sit amet, sed dia consetetur sadipscing elitr, sed diam nonumy eirmod.</p>
    <span class="btn f-btn">Read more</span>
  </div>

  <div class="abs why"></div>
  <div class="abs why-media" role="img" aria-label="Video still of a glass pyramid plaza with visitors"></div>
  <svg class="abs" style="left:403px;top:631px" width="26" height="26" viewBox="0 0 26 26">
    <circle cx="13" cy="13" r="11.5" fill="none" stroke="#fff" stroke-width="2"/>
    <path d="M10 8 L18 13 L10 18Z" fill="#fff"/>
  </svg>
  <h2 class="abs why-title">Why Mesa Ridge HR Consulting.?</h2>
  <p class="abs why-text">Design equidem tibique id duo, movet definiebas at has. Ne duo autem utamur utroque, nusquam dissentias cum ut. In pri putant civibus, nec in homero accusamus. Eam perfecto. Reque scaevola ponderum laudem numquam, audire impedit percipitur. Dico omnis graeco eum cu, patrioque vix ludus . Labitur abhorreant. Luptatum iudicabit his. Quidam semper omittam.<br>Eam perfecto. Reque scaevola ponderum laudem numquam, audire impedit percipitur.</p>
  <span class="abs btn why-btn">Read more</span>

  <footer class="abs footer"></footer>
  <div class="abs f-col" style="left:325px">
    <h3>Quick Links</h3>
    <ul><li>Home</li><li>About Us</li><li>HR Consulting</li><li>News</li><li>Events</li><li>Projects</li><li>Gallery</li><li>Contact us</li></ul>
  </div>
  <div class="abs f-col" style="left:462px">
    <h3>Explore Categories</h3>
    <ul><li>HR Shared Services</li><li>HR Tech</li><li>HR Metrics</li><li>Talent Management</li></ul>
  </div>
  <div class="abs f-col" style="left:600px">
    <h3>Connect With Us</h3>
    <div class="social"><span></span><span></span><span></span><span></span></div>
  </div>
  <div class="abs f-col" style="left:737px">
    <h3>Find Us</h3>
    <div class="find-row">
      <svg width="12" height="12" viewBox="0 0 12 12"><circle cx="6" cy="6" r="5.5" fill="#ddd"/><path d="M3 6.5 L6 3.5 L9 6.5 V9 H3Z" fill="#2f2f2f"/></svg>
      <span>Mesa Ridge HR Consulting,<br>Putant Civibus, Nec Home,<br>Accusamus, Eam Perfecto.</span>
    </div>
    <div class="find-row">
      <svg width="12" height="12" viewBox="0 0 12 12"><circle cx="6" cy="6" r="5.3" fill="none" stroke="#ddd"/><path d="M4 3.2 L5.2 4.6 L4.6 5.4 Q5.4 7 6.6 7.6 L7.4 7 L8.8 8.2 L8 9 Q5 8.6 3.2 4Z" fill="#ddd"/></svg>
      <span>+91 0000 55 120<br>+91 0000 55 120</span>
    </div>
    <div class="find-row">
      <svg width="12" height="12" viewBox="0 0 12 12"><circle cx="6" cy="6" r="5.5" fill="#ddd"/><rect x="3" y="4" width="6" height="4.2" fill="#2f2f2f"/><path d="M3 4 L6 6.4 L9 4" stroke="#ddd" stroke-width=".7" fill="none"/></svg>
      <span>hello@mesaridge.example<br>hello@mesaridge.example</span>
    </div>
  </div>
  <div class="abs f-rule"></div>
  <p class="abs copyright">Copyright 2014 - All rights reserved by Mesa Ridge HR Consulting pvt. ltd.</p>
</div>
</body>
</html>
```